Flyer Personenführungsanlage
Zielgruppe
Unser Unternehmen bietet Kommunikationslösungen rund um Veranstaltungen, Events und Messen an. Für Vorführungen auf Messen, Werksführungen und Dolmetscheraufgaben bieten wir sogenannte "Personenführungsanlagen" zur Miete an. Diese Anlagen bestehen aus einem Handmikrofon oder einem Headset, die Zuhörer erhalten einen Taschenempfänger mit Ohrhörer. Unsere Zielgruppe sind Eventagenturen, Veranstaltungstechnikfirmen, Kirchen, Schwerhörige, sowie Cityguides und Veranstalter.
Aufgabenstellung
Wir möchten für die Personenführungsanlage einen eigenen Produktflyer (max. 4 Seiten) im DIN lang Format 10,5cm x 21,0 cm entwickeln lassen. Alle Informationen und Texte zu diesen Produkten sind auf unserer Webseite. Der Flyer soll die auf der Einführungseite den Anwendungszweck von Personenführungsanlagen erklären, im Anschluss die Produkte Handsender KV-5, Taschenempfänger ZL-3, Ohrhörer MF-4,Kopfhörer MF-6, Induktionsschleife WE-700 sowie den Koffer B72 darstellen, und am Schluss die Einsatzgebiete des Systems (Besichtigungen,Dolmetschertechnik,Hörunterstützung,Effektives Training und Live Kommentare).

```html
<!DOCTYPE html>
<html lang="de">
<head>
<meta charset="utf-8">
<title>Flyer Personenführungsanlage</title>
<link href="https://fonts.googleapis.com/css2?family=Fira+Sans+Extra+Condensed:wght@500;600&family=Open+Sans:wght@400;600&display=swap" rel="stylesheet">
<style>
:root{
  --teal:#1189a8;
  --teal-dark:#0c7590;
  --ink:#1c1c1c;
  --bar:#1e1e1e;
  --grey:#d6d7d9;
  --grey-light:#e9eaeb;
  --bg:#eceeef;
  --white:#ffffff;
}
*{box-sizing:border-box;margin:0;padding:0}
html,body{width:1200px;height:742px;overflow:hidden;background:var(--bg)}
body{position:relative;font-family:"Open Sans",sans-serif;color:var(--ink)}
.head{font-family:"Fira Sans Extra Condensed",sans-serif;font-weight:600}
.panel{position:absolute;background:var(--white);overflow:hidden;box-shadow:0 3px 8px rgba(0,0,0,.25)}
p{font-size:5.6px;line-height:1.45;text-align:justify;margin-bottom:5px}

/* cover */
.cover{left:49px;top:140px;width:237px;height:483px}
.cover .edge{position:absolute;left:0;top:0;width:10px;height:143px;background:var(--teal)}
.cover .edge-low{position:absolute;left:0;top:143px;width:10px;bottom:0;background:var(--grey)}
.brand{position:absolute;right:18px;top:30px;display:flex;align-items:center;gap:5px}
.brand-dot{width:8px;height:8px;border-radius:50%;background:var(--teal)}
.brand-name{font-family:"Fira Sans Extra Condensed",sans-serif;font-weight:600;font-size:26px;color:var(--teal);letter-spacing:.5px}
.cover .photo{position:absolute;left:10px;right:0;top:143px;height:140px;background:linear-gradient(120deg,#c9a874,#8d7a66 45%,#e6ddcd)}
.cover .blue{position:absolute;left:10px;right:0;top:283px;bottom:0;background:var(--teal)}
.cover h1{position:absolute;left:22px;top:300px;font-size:18px;color:var(--white)}

/* back panel */
.back{left:313px;top:100px;width:241px;height:484px}
.band{background:var(--teal);color:var(--white);font-size:12.5px;padding:7px 12px;height:29px}
.subbar{background:var(--bar);color:var(--white);font-size:6.6px;padding:3px 12px;margin:5px 12px 5px 0;border-radius:0 4px 4px 0}
.back .copy{padding:0 12px}
.back .lower{position:absolute;left:0;right:0;top:283px;bottom:0;background:var(--grey)}
.back .lower .tab{position:absolute;left:0;top:120px;width:17px;height:26px;background:var(--white)}
.contact{position:absolute;left:23px;top:120px;font-family:"Fira Sans Extra Condensed",sans-serif;font-weight:500;font-size:6.4px;line-height:1.45}
.contact .gap{height:8px}

/* spread */
.spread{left:608px;top:125px;width:482px;height:480px;background:var(--grey)}
.page-l{position:absolute;left:0;top:0;width:240px;height:480px;background:var(--grey-light)}
.page-r{position:absolute;left:240px;top:0;width:242px;height:480px;background:var(--white)}
.intro{background:var(--white);margin:10px 0 0 0;padding:4px 12px 6px 20px;position:relative}
.intro p{color:var(--teal);margin-bottom:7px}
.intro .marks{position:absolute;left:3px;top:4px;width:6px;bottom:6px;background:linear-gradient(var(--grey) 0 40%,transparent 40% 45%,var(--grey) 45% 70%,transparent 70% 75%,var(--grey) 75%)}
.page-l .band.products{margin-top:8px}
.tiles{position:absolute;left:10px;top:243px;width:222px;height:228px}
.tile{position:absolute;background:var(--white)}
.tile .label{position:absolute;font-family:"Fira Sans Extra Condensed",sans-serif;font-weight:600;font-size:7.4px;color:var(--teal-dark)}
.tile .shape{position:absolute;background:linear-gradient(135deg,#cfd2d5,#8f9398)}
.page-r .top{position:absolute;left:0;top:0;width:242px;height:125px;background:linear-gradient(180deg,#f4f4f5,#d9dadc)}
.page-r .band{position:absolute;left:0;right:0;top:139px}
.page-r .copy-r{position:absolute;left:0;right:0;top:172px;padding-left:0}
.page-r .subbar{margin-left:0;padding-left:12px}
.page-r p{padding:0 12px}
</style>
</head>
<body>

<section class="panel cover">
  <div class="edge"></div><div class="edge-low"></div>
  <div class="brand"><span class="brand-dot"></span><span class="brand-name">VENTARIS</span></div>
  <div class="photo" role="img" aria-label="Foto: Gästeführerin mit Handmikrofon, Zuhörer mit Ohrhörern"></div>
  <div class="blue"></div>
  <h1 class="head">Personenführungsanlage</h1>
</section>

<section class="panel back">
  <div class="band head">Einsatzgebiete</div>
  <div class="subbar head">Kommandoanlage für effektives Training</div>
  <div class="copy">
    <p>Überall wo Trainingsinhalte übermittelt werden sollen, ist Aurivox Ihr optimaler Begleiter:</p>
    <p>Ob beim Pferdesport, beim Rudersport, am Hundeübungsplatz, am Verkehrsübungsplatz oder bei Unterweisungen an großen und lauten Maschinen – mit Aurivox als Kommandoanlage werden die Anweisungen des Trainers und Experten auch über weitere Entfernungen verstanden und die Übungen können optimal umgesetzt werden.</p>
  </div>
  <div class="subbar head">Übertragungssystem für Live Kommentare für Sehbehinderte</div>
  <div class="copy">
    <p>Sorgen Sie für Gleichberechtigung und schließen Sie keine Fans aus.</p>
    <p>Durch spezielle Live-Kommentare können Sehbehinderte z.B. bei Sportveranstaltungen dem Geschehen folgen und dabei an der Stimmung im Stadion unmittelbar teilhaben.</p>
    <p>Mit dem drahtlosen Übertragungssystem Aurivox werden die Kommentare sicher und mit optimaler Sprachverständlichkeit an die Besucher übertragen.</p>
  </div>
  <div class="lower">
    <div class="tab"></div>
    <div class="contact">
      VENTARIS<br>Kastanienallee 12<br>73614 Beispielheim
      <div class="gap"></div>
      Telefon: (07150) 48 27 10<br>Fax: (07150) 48 27 11
      <div class="gap"></div>
      www.ventaris-rental.de
    </div>
  </div>
</section>

<section class="panel spread">
  <div class="page-l">
    <div class="band head">Führungsanlage</div>
    <div class="intro">
      <div class="marks"></div>
      <p>Das gesprochene Wort ist bei der Übertragung von Informationen unerlässlich: Ob im kleinen Personenkreis oder innerhalb großer Gruppen. Egal ob bei Werks- oder Stadtführungen, Bus- oder Schiffsreisen, Dolmetscher- bzw. Hörunterstützung oder Trainings – die optimale Verständigung mit Ihren Gästen ist unerlässlich.</p>
      <p>Bei diesen Anforderungen werden zur Unterstützung sogenannte Führungsanlagen oder auch Flüsteranlagen eingesetzt.</p>
      <p>Es gibt zahlreiche Systeme von unterschiedlichsten Herstellern am Markt. Eines der modernsten Systeme auch in Punkto Zuverlässigkeit, Robustheit und Einfachheit in der Bedienung ist das Tour Guide System Aurivox aus dem Hause Tonwerk.</p>
      <p>Wir vermieten das Tonwerk Aurivox System – das grosse Spektrum der Anwendungsmöglichkeiten sowie die breite Auswahl an Zubehör haben uns von diesem System überzeugt.</p>
    </div>
    <div class="band head products">Produkte</div>
    <div class="tiles">
      <div class="tile" style="left:0;top:0;width:104px;height:105px;border-radius:22px 22px 0 22px">
        <div class="shape" role="img" aria-label="Produktfoto Handsender" style="left:26px;top:24px;width:56px;height:14px;border-radius:7px;transform:rotate(-35deg);top:44px"></div>
        <span class="label" style="right:4px;bottom:4px">Handsender KV-5</span>
      </div>
      <div class="tile" style="left:113px;top:0;width:109px;height:105px;border-radius:22px 0 0 0">
        <div class="shape" role="img" aria-label="Produktfoto Ohrhörer" style="left:10px;top:26px;width:26px;height:34px;border-radius:50%"></div>
        <span class="label" style="left:4px;bottom:4px">Ohrhörer MF-4</span>
      </div>
      <div class="tile" style="left:0;top:112px;width:104px;height:94px;border-radius:0 0 22px 0">
        <span class="label" style="right:4px;top:3px">Taschenempfänger ZL-3</span>
        <div class="shape" role="img" aria-label="Produktfoto Taschenempfänger" style="left:36px;top:24px;width:26px;height:44px;border-radius:4px"></div>
      </div>
      <div class="tile" style="left:113px;top:112px;width:109px;height:116px;border-radius:0 22px 0 0;background:linear-gradient(180deg,#fff,#eeeff0)">
        <span class="label" style="left:4px;top:3px">Kopfhörer MF-6</span>
        <div class="shape" role="img" aria-label="Produktfoto Kopfhörer" style="left:20px;top:24px;width:62px;height:70px;border-radius:31px 31px 8px 8px;background:none;border:4px solid #555"></div>
      </div>
    </div>
  </div>
  <div class="page-r">
    <div class="top">
      <div class="tile" style="left:8px;top:0;width:88px;height:120px;border-radius:0 0 0 20px">
        <span class="label" style="left:5px;top:10px">Induktionsschleife WE-700</span>
        <div class="shape" role="img" aria-label="Produktfoto Induktionsschleife" style="left:22px;top:28px;width:44px;height:70px;border-radius:22px 22px 22px 22px;background:none;border:2px solid #666"></div>
      </div>
      <div class="tile" style="left:100px;top:28px;width:142px;height:92px;border-radius:20px 0 0 0;background:linear-gradient(180deg,#fff,#e4e5e6)">
        <span class="label" style="right:8px;top:4px">Koffer B72</span>
        <div class="shape" role="img" aria-label="Produktfoto Transportkoffer mit Zubehör" style="left:8px;top:18px;width:78px;height:64px;border-radius:4px"></div>
      </div>
    </div>
    <div class="band head">Einsatzgebiete</div>
    <div class="copy-r">
      <div class="subbar head">Führungen / Besichtigungen</div>
      <p>Durch persönliche Führungen wird die Besichtigung zum individuellen Erlebnis für Ihre Gäste. Mit der Besucherführungsanlage Aurivox können mehrere Gruppen gleichzeitig unabhängig voneinander an Führungen teilnehmen. Jeder Besucher kann seine Lautstärke individuell einstellen. Bei Besuchern mit Hörgeräten kann der Ton durch eine Induktionsschleife direkt auf das eigene Hörgerät übertragen werden.</p>
      <div class="subbar head">Dolmetschersystem und mobile Flüsteranlage</div>
      <p>Als Dolmetschersystem wird Aurivox für zwei Anwendungsbereiche eingesetzt:</p>
      <p>Im Zusammenhang mit Dolmetschertechnik dient Aurivox zur drahtlosen Übertragung der Fremdsprachen an die Konferenzteilnehmer. Die Teilnehmer wählen einfach den Kanal für ihre Sprache aus.</p>
      <p>Beim Flüsterdolmetschen wird Aurivox als mobile Flüsteranlage eingesetzt. Hierbei bietet die individuell einstellbare Stummschaltung des Handsenders optimale Arbeitsbedingungen für Dolmetscher.</p>
      <div class="subbar head">Schwerhörigenanlage zur Hörunterstützung in öffentlichen Einrichtungen</div>
      <p>Barrierefreies Hören in Schulen, Kirchen, Kinos, Theatern oder Stadien leicht gemacht: Mit dem Aurivox Drahtlossystem zur Hörunterstützung wird der Beitrag akustisch verstärkt.</p>
      <p>Anstelle des Hörers können auch Induktionsschleifen für Hörgeräte mit Induktionsspulen eingesetzt werden. Mit Aurivox als Schwerhörigen-anlage werden Sie bei Veranstaltungen immer jedes Wort verstehen.</p>
    </div>
  </div>
</section>

</body>
</html>
```